New website

We ned to create a new website that reflects more who we are. We are delivering exclusive premium products to our customers and the current website does not reflect our products at all.
We believe in less is more and need a webpage that is clean yet professional and exclusive.

Target Market(s)

Dentistry

Industry/Entity Type

Dental

Number of Pages Required

5+ page

Font styles to use
Sans Serif

Colors

Designer to choose colors to be used in the design.

Requirements
Must have
• Picture gallery
• Nice structure
• Clean layout
Nice to have
• Light fonts
Should not have
• Any italic font styles

```html
<!DOCTYPE html>
<html lang="en">
<head>
<meta charset="utf-8">
<title>Norvik Dental – Winning Precision</title>
<link href="https://fonts.googleapis.com/css2?family=Jost:wght@300;400;500;600&family=Open+Sans:wght@400;600&display=swap" rel="stylesheet">
<style>
:root{
  --red:#e8232a;
  --blue:#2a5aa8;
  --link-blue:#2b62b5;
  --ink:#222;
  --text:#444;
  --muted:#777;
  --rule:#d9d9d9;
  --light:#f4f4f4;
  --dark:#232628;
  --footer:#1b1b1b;
  --white:#fff;
}
*{box-sizing:border-box;margin:0;padding:0}
html,body{width:1200px;height:2597px;overflow:hidden}
body{font-family:"Jost",sans-serif;color:var(--text);background:var(--white);position:relative}
h1,h2,h3,h4{font-weight:400}
a{color:inherit;text-decoration:none}

/* header */
.topbar{position:absolute;left:0;top:0;width:1200px;height:54px;background:var(--white)}
.brand{position:absolute;left:105px;top:14px;width:250px;height:70px;background:var(--white);border-radius:0 0 18px 18px;z-index:3;display:flex;align-items:center;justify-content:center;gap:10px}
.brand-dot{width:14px;height:14px;border-radius:50%;background:var(--red)}
.brand-name{font-size:25px;font-weight:400;color:var(--ink)}
.call{position:absolute;left:806px;top:17px;font-size:15px;color:var(--ink);display:flex;align-items:center;gap:8px}
.lang{position:absolute;left:1029px;top:11px;width:72px;height:32px;border:1px solid var(--rule);display:flex;align-items:center;justify-content:center;gap:8px}
.lang-swatch{width:24px;height:15px;background:linear-gradient(#2d4b8f,#c8303a)}
.nav{position:absolute;left:0;top:54px;width:1200px;height:43px;background:var(--blue)}
.nav ul{list-style:none;position:absolute;left:398px;top:0;display:flex;height:43px}
.nav li{font-size:15px;color:var(--white);padding:0 11px;line-height:43px}
.nav li.active{background:var(--red);padding:0 24px}

/* hero */
.hero{position:absolute;left:0;top:97px;width:1200px;height:545px;background:linear-gradient(100deg,#dfe6ea 0%,#c9dbe2 35%,#e9e4df 60%,#d8c2b2 100%)}
.hero-title{position:absolute;left:99px;top:198px;color:var(--white);font-size:37px;font-weight:500;line-height:45px;text-shadow:0 2px 6px rgba(0,0,0,.35);letter-spacing:.5px}
.hero-arrow{position:absolute;top:230px;width:28px;height:34px;background:rgba(255,255,255,.55);display:flex;align-items:center;justify-content:center}
.hero-dots{position:absolute;left:573px;top:494px;display:flex;gap:8px;align-items:center}
.dot{width:11px;height:11px;border-radius:50%;background:rgba(255,255,255,.7)}
.dot.on{width:16px;height:16px;border:2px solid var(--white);background:var(--red)}

/* section titles */
.section-title{position:absolute;left:0;width:1200px;text-align:center;font-size:29px;font-weight:500;color:var(--ink);text-transform:uppercase}
.section-title em{font-style:normal;color:var(--red)}
.divider{position:absolute;left:484px;width:232px;height:12px}
.divider::before{content:"";position:absolute;left:0;right:0;top:5px;height:2px;background:var(--rule)}
.divider::after{content:"";position:absolute;left:102px;top:0;width:28px;height:12px;background:#cfcfcf;box-shadow:0 0 0 5px var(--bg,#fff)}

/* services */
.services{position:absolute;left:0;top:642px;width:1200px;height:539px;background:var(--white)}
.lede{position:absolute;left:265px;top:133px;width:670px;text-align:center;font-family:"Open Sans",sans-serif;font-size:13px;line-height:22px;color:var(--text)}
.service-card{position:absolute;top:198px;width:299px;height:280px;border:1px solid #ddd;border-radius:3px;background:#fff;text-align:center;box-shadow:0 2px 4px rgba(0,0,0,.05)}
.service-card.featured{background:var(--red);border:none}
.service-card.featured::before{content:"";position:absolute;inset:8px;border:2px solid rgba(255,255,255,.8);border-radius:2px}
.service-name{margin-top:14px;font-size:22px;font-weight:400;color:var(--ink)}
.featured .service-name,.featured .service-desc{color:var(--white)}
.service-icon{width:120px;height:120px;border-radius:50%;margin:20px auto 0;background:radial-gradient(#f1f1f1,#d8d8d8);border:6px solid #fff;box-shadow:0 0 0 2px #ddd}
.featured .service-icon{background:radial-gradient(#e0282f,#b81419);box-shadow:0 0 0 2px rgba(255,255,255,.8)}
.service-desc{font-family:"Open Sans",sans-serif;font-size:12px;line-height:20px;color:var(--ink);margin:20px auto 0;width:250px}
.read-tab{position:absolute;left:74px;bottom:0;width:150px;height:30px;background:#eee;color:var(--ink);font-size:14px;line-height:30px;clip-path:polygon(10% 0,90% 0,100% 100%,0 100%)}
.featured .read-tab{background:#333;color:#fff;bottom:6px}
.side-arrow{position:absolute;width:40px;height:70px}

/* gallery */
.gallery{position:absolute;left:0;top:1181px;width:1200px;height:478px;background:var(--light);--bg:var(--light)}
.smile-card{position:absolute;top:144px;width:327px;height:268px;background:#fff;box-shadow:0 1px 4px rgba(0,0,0,.08);text-align:center}
.smile-photos{display:flex;gap:4px;margin:10px 10px 0}
.smile-photo{position:relative;flex:1;height:118px;background:linear-gradient(180deg,#8a4a3e 0%,#c98a7a 35%,#efe4cf 55%,#b0605a 80%,#7a3a32 100%)}
.smile-tag{position:absolute;left:0;bottom:0;background:rgba(60,40,35,.75);color:#fff;font-size:13px;padding:3px 8px}
.smile-title{margin-top:14px;font-size:19px;font-weight:400;color:var(--link-blue)}
.smile-desc{font-family:"Open Sans",sans-serif;font-size:12px;line-height:20px;color:var(--text);margin:12px auto 0;width:290px}
.smile-pager{position:absolute;left:143px;bottom:-8px;display:flex;gap:6px}
.smile-pager span{width:16px;height:16px;border-radius:50%;background:#ddd}
.smile-pager.on span{background:var(--red)}

/* call to action */
.cta{position:absolute;left:0;top:1659px;width:1200px;height:156px;background:var(--dark)}
.cta-text{position:absolute;left:101px;top:45px;color:#fff;font-size:20px;line-height:34px}
.cta-btn{position:absolute;left:930px;top:59px;width:134px;height:38px;background:var(--red);color:#fff;font-size:16px;line-height:38px;text-align:center}
.cta-btn-tail{position:absolute;left:1068px;top:59px;width:33px;height:38px;background:#555}

/* blog + testimonials */
.news{position:absolute;left:0;top:1815px;width:1200px;height:381px;background:#fff}
.col-title{position:absolute;font-size:27px;font-weight:500;color:var(--ink);text-transform:uppercase}
.col-title em{font-style:normal;color:var(--red)}
.col-rule{position:absolute;height:2px;background:var(--rule)}
.col-rule::before{content:"";position:absolute;left:-20px;top:-5px;width:26px;height:11px;background:#cfcfcf}
.post{position:absolute;left:99px;width:470px}
.post-date{position:absolute;left:0;top:0;width:46px;height:46px;border:1px solid #ccc;text-align:center}
.post-day{font-size:22px;color:var(--ink);line-height:28px}
.post-month{position:absolute;left:0;bottom:0;width:100%;background:var(--blue);color:#fff;font-size:9px;line-height:14px}
.post-title{position:absolute;left:70px;top:0;font-size:17px;font-weight:400;color:var(--ink);white-space:nowrap}
.post-text{position:absolute;left:70px;top:28px;width:410px;font-family:"Open Sans",sans-serif;font-size:11.5px;line-height:20px;color:var(--text)}
.post-rule{position:absolute;left:0;top:86px;width:470px;height:1px;background:var(--rule)}
.more-btn{position:absolute;left:457px;top:284px;width:114px;height:34px;background:var(--red);color:#fff;font-size:15px;line-height:34px;text-align:center}
.more-tail{position:absolute;left:575px;top:284px;width:28px;height:34px;background:var(--blue)}
.quote-mark{position:absolute;left:689px;top:112px;font-size:48px;color:#bbb;line-height:40px;font-family:"Open Sans",sans-serif}
.quote{position:absolute;left:740px;top:106px;width:362px;font-family:"Open Sans",sans-serif;font-size:12px;line-height:22px;color:var(--text)}
.quote-rule{position:absolute;left:693px;top:236px;width:300px;height:2px;background:var(--rule)}
.author{position:absolute;left:820px;top:244px;width:155px;text-align:right}
.author-name{font-size:16px;color:var(--ink);text-transform:uppercase}
.author-role{font-family:"Open Sans",sans-serif;font-size:12px;color:var(--muted)}
.avatar{position:absolute;left:988px;top:206px;width:96px;height:96px;border-radius:50%;border:4px solid #fff;box-shadow:0 0 0 1px #ddd;background:linear-gradient(160deg,#c9d6e3,#6d8aa8)}
.pager{position:absolute;top:285px;width:28px;height:28px;display:flex;align-items:center;justify-content:center}

/* footer */
.footer{position:absolute;left:0;top:2196px;width:1200px;height:346px;background:var(--footer);color:#bbb}
.foot-head{position:absolute;top:66px;font-size:19px;font-weight:400;color:#fff}
.foot-line{position:absolute;top:104px;width:60px;height:1px;background:#555}
.quick{position:absolute;left:100px;top:118px;list-style:none;font-family:"Open Sans",sans-serif;font-size:13px;line-height:27.7px}
.quick li::before{content:"›";margin-right:8px;color:#888}
.about{position:absolute;left:339px;top:118px;width:408px;font-family:"Open Sans",sans-serif;font-size:13px;line-height:27.7px}
.about u{color:#fff}
.vsep{position:absolute;top:110px;width:1px;height:190px;background:#2e2e2e}
.contact{position:absolute;left:880px;top:114px;width:230px;font-family:"Open Sans",sans-serif;font-size:13px;color:#ccc}
.contact-row{position:relative;padding-left:32px;margin-bottom:16px;line-height:18px}
.contact-row svg{position:absolute;left:0;top:2px}
.contact-row strong{font-weight:400;color:#fff;font-size:14px}
.bottombar{position:absolute;left:0;top:2542px;width:1200px;height:55px;background:var(--red);color:#fff}
.copyright{position:absolute;left:101px;top:18px;font-size:15px}
.follow{position:absolute;left:875px;top:15px;display:flex;align-items:center;gap:7px;font-size:16px;font-weight:500}
.follow span.circle{width:26px;height:26px;border-radius:50%;background:var(--blue);border:2px solid #fff}
.follow span.circle.alt{background:#f08a1c}
</style>
</head>
<body>

<header class="topbar">
  <div class="brand"><span class="brand-dot"></span><span class="brand-name">Norvik Dental</span></div>
  <div class="call">
    <svg width="14" height="14" viewBox="0 0 24 24"><path fill="#e8232a" d="M6.6 10.8a15.1 15.1 0 006.6 6.6l2.2-2.2a1 1 0 011-.25 11.4 11.4 0 003.6.57 1 1 0 011 1V20a1 1 0 01-1 1A17 17 0 013 4a1 1 0 011-1h3.5a1 1 0 011 1c0 1.25.2 2.45.57 3.57a1 1 0 01-.25 1z"/></svg>
    Call Us +46-40-12 34 56
  </div>
  <div class="lang"><span class="lang-swatch"></span><svg width="10" height="6" viewBox="0 0 10 6"><path d="M1 1l4 4 4-4" stroke="#333" fill="none" stroke-width="1.5"/></svg></div>
</header>
<nav class="nav">
  <ul>
    <li class="active">Home</li><li>The Company</li><li>Products</li><li>Our Services</li><li>Smile Gallery</li><li>Shade Analysis</li><li>Contact Us</li>
  </ul>
</nav>

<section class="hero" role="img" aria-label="Smiling couple on a beach">
  <h1 class="hero-title">NORVIK DENTAL &amp;<br>WINNING PRECISION</h1>
  <div class="hero-arrow" style="left:0"><svg width="10" height="14" viewBox="0 0 10 14"><path d="M8 1L2 7l6 6" stroke="#fff" stroke-width="2" fill="none"/></svg></div>
  <div class="hero-arrow" style="left:1172px"><svg width="10" height="14" viewBox="0 0 10 14"><path d="M2 1l6 6-6 6" stroke="#fff" stroke-width="2" fill="none"/></svg></div>
  <div class="hero-dots"><span class="dot"></span><span class="dot on"></span><span class="dot"></span></div>
</section>

<section class="services">
  <h2 class="section-title" style="top:50px">Our <em>Services</em></h2>
  <div class="divider" style="top:102px"></div>
  <p class="lede">Norvik Dental ensures exact teeth reconstruction, individual service of the customer and technical information. We can also offer our customers additional service on favorable terms.</p>
  <svg class="side-arrow" style="left:40px;top:310px" viewBox="0 0 40 70"><path d="M34 4L6 35l28 31" stroke="#ccc" stroke-width="1.5" fill="none"/></svg>
  <svg class="side-arrow" style="left:1120px;top:310px" viewBox="0 0 40 70"><path d="M6 4l28 31L6 66" stroke="#ccc" stroke-width="1.5" fill="none"/></svg>

  <article class="service-card" style="left:99px">
    <h3 class="service-name">Cosmetic Imaging</h3>
    <div class="service-icon" role="img" aria-label="Tooth icon"></div>
    <p class="service-desc">Norvik Dental offers an advanced cosmetic imaging system designed....</p>
    <a class="read-tab">Read More</a>
  </article>
  <article class="service-card featured" style="left:450px">
    <h3 class="service-name">Diagnostic Wax Up</h3>
    <div class="service-icon" role="img" aria-label="Tooth icon"></div>
    <p class="service-desc">The diagnostic wax-up is a tool enjoying success, if it is the matter....</p>
    <a class="read-tab">Read More</a>
  </article>
  <article class="service-card" style="left:802px">
    <h3 class="service-name">Color test veneer</h3>
    <div class="service-icon" role="img" aria-label="Veneer icon"></div>
    <p class="service-desc">If a good color effect on the enamel affected by chromatism is for you....</p>
    <a class="read-tab">Read More</a>
  </article>
</section>

<section class="gallery">
  <h2 class="section-title" style="top:52px">Smile <em>Gallery</em></h2>
  <div class="divider" style="top:104px"></div>
  <svg class="side-arrow" style="left:34px;top:246px" viewBox="0 0 40 70"><path d="M34 4L6 35l28 31" stroke="#ccc" stroke-width="1.5" fill="none"/></svg>
  <svg class="side-arrow" style="left:1126px;top:246px" viewBox="0 0 40 70"><path d="M6 4l28 31L6 66" stroke="#ccc" stroke-width="1.5" fill="none"/></svg>

  <article class="smile-card" style="left:99px">
    <div class="smile-photos">
      <div class="smile-photo" role="img" aria-label="Teeth before treatment"><span class="smile-tag">Before</span></div>
      <div class="smile-photo" role="img" aria-label="Teeth after veneers"><span class="smile-tag">After</span></div>
    </div>
    <h3 class="smile-title">SMILE 1 - Norvik Veneers</h3>
    <p class="smile-desc">This patient had problems with seveere crooked teeth that made the smile unaesthetic.</p>
    <div class="smile-pager"><span></span><span></span></div>
  </article>
  <article class="smile-card" style="left:435px">
    <div class="smile-photos">
      <div class="smile-photo" role="img" aria-label="Teeth before treatment"><span class="smile-tag">Before</span></div>
      <div class="smile-photo" role="img" aria-label="Teeth after zirconia bridge"><span class="smile-tag">After</span></div>
    </div>
    <h3 class="smile-title">SMILE 2 - Zirconia bridge</h3>
    <p class="smile-desc">This patient needed to replace her lateral. Norvik provided a high strenght ...</p>
    <div class="smile-pager on"><span></span><span></span></div>
  </article>
  <article class="smile-card" style="left:772px">
    <div class="smile-photos">
      <div class="smile-photo" role="img" aria-label="Teeth before treatment"><span class="smile-tag">Before</span></div>
      <div class="smile-photo" role="img" aria-label="Teeth after ceramic crowns"><span class="smile-tag">After</span></div>
    </div>
    <h3 class="smile-title">SMILE 3 - Ceramic Crowns</h3>
    <p class="smile-desc">This patient had problems with seveere discoloration and with filling</p>
    <div class="smile-pager"><span></span><span></span></div>
  </article>
</section>

<section class="cta">
  <p class="cta-text">Ask About Our Service &nbsp;And Care.<br>To Make An Appointment Please Call Us On +46-40-12 34 56</p>
  <a class="cta-btn">Contact Us</a><span class="cta-btn-tail"></span>
</section>

<section class="news">
  <h2 class="col-title" style="left:99px;top:44px">Latest <em>Blog</em></h2>
  <div class="col-rule" style="left:323px;top:62px;width:240px"></div>
  <article class="post" style="top:112px">
    <div class="post-date"><div class="post-day">20</div><div class="post-month">APR-16</div></div>
    <h3 class="post-title">Lorem lipsum is simpaly dummy text of the printing ind</h3>
    <p class="post-text">Lorem Ipsum is simply dummy text of the printing and typesetting industry. Lore Ipsum has been the industry's standard dummy text... [+]</p>
    <div class="post-rule"></div>
  </article>
  <article class="post" style="top:211px">
    <div class="post-date"><div class="post-day">25</div><div class="post-month">APR-16</div></div>
    <h3 class="post-title">Lorem lipsum is simpaly dummy text of the printing ind</h3>
    <p class="post-text">Lorem Ipsum is simply dummy text of the printing and typesetting industry. Lore Ipsum has been the industry's standard dummy text... [+]</p>
  </article>
  <a class="more-btn">Read More</a><span class="more-tail"></span>

  <h2 class="col-title" style="left:686px;top:44px">Client <em>Testimonials</em></h2>
  <div class="col-rule" style="left:1038px;top:62px;width:63px"></div>
  <div class="quote-mark">“</div>
  <p class="quote">" Lorem Ipsum is simply dummy text of the printing and type setting industry. Lorem Ipsum has been the industry's standard dummy text ever since the 1500s, when an unknown printer took a galley of type and scrambled it to ..."</p>
  <div class="quote-rule"></div>
  <div class="author"><div class="author-name">Elin Marsh</div><div class="author-role">Voluptate velit</div></div>
  <div class="avatar" role="img" aria-label="Client portrait"></div>
  <span class="pager" style="left:689px;background:var(--red)"><svg width="8" height="12" viewBox="0 0 8 12"><path d="M6 1L2 6l4 5" stroke="#fff" stroke-width="2" fill="none"/></svg></span>
  <span class="pager" style="left:722px;background:#ccc"><svg width="8" height="12" viewBox="0 0 8 12"><path d="M2 1l4 5-4 5" stroke="#fff" stroke-width="2" fill="none"/></svg></span>
</section>

<footer class="footer">
  <h4 class="foot-head" style="left:100px">Quick Links</h4><div class="foot-line" style="left:100px"></div>
  <ul class="quick">
    <li>Home</li><li>The Company</li><li>Products</li><li>Our Services</li><li>Smile Gallery</li><li>Shade Analysis</li><li>Contact Us</li>
  </ul>
  <div class="vsep" style="left:276px"></div>
  <h4 class="foot-head" style="left:339px">About Norvik Dental</h4>
  <p class="about">Who designed this Smile?<br>Norvik smiles has a very distinctive appearance and character. Both these Norvik features owe as much to their owners as to our dental artisans, because in the final analysis, people who buy a new smile also designs them.Inevitably, the greater the demands a smile has to meet, the lower the lowest denominator... <u>Read More</u></p>
  <div class="vsep" style="left:818px"></div>
  <h4 class="foot-head" style="left:880px">Contact Details</h4>
  <div class="contact">
    <div class="contact-row"><svg width="14" height="18" viewBox="0 0 14 18"><path fill="#fff" d="M7 0a7 7 0 00-7 7c0 5 7 11 7 11s7-6 7-11a7 7 0 00-7-7zm0 9.5A2.5 2.5 0 117 4.5a2.5 2.5 0 010 5z"/></svg><strong>Norvik Dental AB</strong><br>Box 10050 21120 Malmö,<br>Sweden</div>
    <div class="contact-row" style="margin-top:24px"><svg width="14" height="14" viewBox="0 0 24 24"><path fill="#fff" d="M6.6 10.8a15.1 15.1 0 006.6 6.6l2.2-2.2a1 1 0 011-.25 11.4 11.4 0 003.6.57 1 1 0 011 1V20a1 1 0 01-1 1A17 17 0 013 4a1 1 0 011-1h3.5a1 1 0 011 1c0 1.25.2 2.45.57 3.57a1 1 0 01-.25 1z"/></svg>+46-40-12 34 56</div>
    <div class="contact-row" style="margin-top:24px"><svg width="15" height="12" viewBox="0 0 15 12"><rect width="15" height="12" fill="#fff"/><path d="M0 0l7.5 6L15 0" stroke="#1b1b1b" fill="none"/></svg>info@norvikdental.com</div>
  </div>
</footer>
<div class="bottombar">
  <p class="copyright">Copyright © 2017 Norvik Dental AB. All Right Reserved.</p>
  <div class="follow">Follow Us <span class="circle"></span><span class="circle"></span><span class="circle"></span><span class="circle alt"></span></div>
</div>

</body>
</html>
```